Criação de Folder para Rubim & Cardoso
A empresa queria:
" FECHANDO CONTRATOS COM O PÚBLICO ALVO PARA RETIRADA DE MATERIAL RECICLÁVEL E, PRESTANDO SERVIÇOS DIFERENTES AO PROPORCIONADO PELO MERCADO ATUAL "

```html
<!DOCTYPE html>
<html lang="pt-BR">
<head>
<meta charset="UTF-8">
<title>Folder Rubim &amp; Cardoso</title>
<link href="https://fonts.googleapis.com/css2?family=Montserrat:wght@300;400;600;700;800&display=swap" rel="stylesheet">
<style>
  :root{
    --bg:#e9e6e1;
    --paper:#ffffff;
    --ink:#3b3b3b;
    --grey:#8c8c8c;
    --light-grey:#d9d9d9;
    --orange:#ef7d1a;
    --orange-dark:#d9650a;
    --blue:#1fa2d8;
    --red:#e2393f;
    --green:#2aa65c;
    --yellow:#f4c51b;
    --bin-grey:#8a8a8a;
  }
  *{box-sizing:border-box;margin:0;padding:0}
  html,body{width:1200px;height:1200px;overflow:hidden}
  body{background:var(--bg);font-family:"Montserrat",sans-serif;color:var(--ink);position:relative}

  .page{position:absolute;top:190px;width:540px;height:820px;background:var(--paper);overflow:hidden;box-shadow:0 6px 18px rgba(0,0,0,.12)}
  .page--front{left:50px}
  .page--back{left:610px}

  .top-band{position:absolute;left:0;top:0;width:100%;height:56px;background:var(--light-grey)}
  .top-band::after{content:"";position:absolute;left:0;bottom:0;width:100%;height:8px;background:var(--grey)}

  /* front */
  .brand{position:absolute;left:40px;top:96px;display:flex;align-items:center;gap:14px}
  .brand__mark{width:40px;height:40px;background:var(--orange)}
  .brand__name{font-size:38px;font-weight:800;color:var(--ink);letter-spacing:-.5px}
  .brand__tag{position:absolute;left:94px;top:150px;font-size:12px;font-weight:600;letter-spacing:2px;color:var(--grey)}

  .headline{position:absolute;left:40px;top:210px;width:330px;font-size:15px;font-weight:300;line-height:1.6;letter-spacing:1px;text-transform:uppercase;color:var(--grey);padding-left:14px;border-left:3px solid var(--orange)}

  .audience{position:absolute;left:40px;top:420px;list-style:none}
  .audience li{display:flex;align-items:center;gap:10px;font-size:14px;font-weight:600;color:var(--ink);margin-bottom:22px;letter-spacing:1px}
  .audience svg{width:18px;height:18px}

  .actions{position:absolute;left:200px;top:400px;width:305px}
  .action{margin-bottom:16px;padding-bottom:10px;border-bottom:1px solid var(--orange)}
  .action__title{font-size:11px;font-weight:800;letter-spacing:1px;margin-bottom:4px}
  .action__text{font-size:9.5px;line-height:1.45;color:var(--grey)}

  .recycle-art{position:absolute;left:300px;top:612px;width:170px;height:96px;border-radius:8px;background:radial-gradient(circle at 50% 50%,#6b6b6b 0,#bdbdbd 60%,#ededed 100%)}

  .footer{position:absolute;left:0;bottom:0;width:100%;height:100px;background:var(--orange)}
  .footer::before{content:"";position:absolute;left:0;top:-10px;width:100%;height:4px;background:var(--orange)}
  .footer__mark{position:absolute;left:40px;top:28px;width:44px;height:44px;border-radius:50%;background:var(--orange-dark)}
  .footer__contacts{position:absolute;left:110px;top:24px;list-style:none;color:#fff;font-size:11px;line-height:1.7}

  /* back */
  .back-title{position:absolute;left:30px;top:72px;font-size:10px;font-weight:700;letter-spacing:2px;color:var(--grey);text-transform:uppercase}
  .bins{position:absolute;left:30px;top:100px;width:230px}
  .bin{display:flex;align-items:center;gap:10px;height:80px}
  .bin__icon{width:34px;height:40px;border-radius:3px;display:flex;align-items:center;justify-content:center}
  .bin__icon svg{width:18px;height:18px}
  .bin__label{position:absolute;font-size:9px;font-weight:700;color:#fff;padding:2px 6px;margin-top:-58px}
  .bin__items{width:150px;height:50px;border-radius:6px;background:linear-gradient(135deg,#e8e8e8,#c9c9c9)}
  .is-blue{background:var(--blue)}
  .is-red{background:var(--red)}
  .is-green{background:var(--green)}
  .is-yellow{background:var(--yellow)}
  .is-grey{background:var(--bin-grey)}

  .guide{position:absolute;left:280px;top:120px;width:235px;border-collapse:collapse}
  .guide th{font-size:10px;font-weight:700;color:var(--orange);text-align:left;padding:0 8px 8px;letter-spacing:1px}
  .guide td{width:50%;height:70px;color:#fff;font-size:9.5px;font-weight:600;padding:8px;vertical-align:middle;border:2px solid #fff}

  .note{position:absolute;left:30px;top:520px;width:230px;background:#f0f0f0;padding:14px;font-size:10px;color:var(--ink);line-height:1.5;border-left:4px solid var(--orange)}

  .back-footer{position:absolute;left:0;bottom:0;width:100%;height:22px;background:var(--orange)}
</style>
</head>
<body>

<section class="page page--front">
  <div class="top-band"></div>

  <div class="brand">
    <span class="brand__mark"></span>
    <span class="brand__name">Rubim &amp; Cardoso</span>
  </div>
  <p class="brand__tag">RECICLÁVEL / SUSTENTÁVEL</p>

  <p class="headline">Fornecemos serviços ao público para retirada de resíduos recicláveis, prestando serviços diferentes do proporcionado pelo mercado</p>

  <ul class="audience">
    <li><svg viewBox="0 0 20 20"><path d="M3 10l5 5L17 4" fill="none" stroke="var(--orange)" stroke-width="3"/></svg>CONDOMÍNIO</li>
    <li><svg viewBox="0 0 20 20"><path d="M3 10l5 5L17 4" fill="none" stroke="var(--orange)" stroke-width="3"/></svg>NEGÓCIO</li>
    <li><svg viewBox="0 0 20 20"><path d="M3 10l5 5L17 4" fill="none" stroke="var(--orange)" stroke-width="3"/></svg>RESIDÊNCIA</li>
  </ul>

  <div class="actions">
    <div class="action">
      <h3 class="action__title">REUTILIZANDO</h3>
      <p class="action__text">Damos nova função a embalagens e objetos, evitando o descarte e prolongando a vida útil de cada material.</p>
    </div>
    <div class="action">
      <h3 class="action__title">REDUZINDO</h3>
      <p class="action__text">Orientamos clientes a consumir com consciência, diminuindo o volume de resíduos gerados no dia a dia.</p>
    </div>
    <div class="action">
      <h3 class="action__title">RECICLANDO</h3>
      <p class="action__text">Coletamos e separamos os materiais recicláveis, devolvendo matéria-prima à indústria com responsabilidade.</p>
    </div>
  </div>

  <div class="recycle-art" role="img" aria-label="Ilustração de ciclo de reciclagem com setas e materiais"></div>

  <footer class="footer">
    <span class="footer__mark"></span>
    <ul class="footer__contacts">
      <li>Rua das Acácias, 120 – Centro</li>
      <li>(11) 4000-1234</li>
      <li>contato@rubimcardoso.com.br</li>
    </ul>
  </footer>
</section>

<section class="page page--back">
  <div class="top-band"></div>
  <p class="back-title">Como separar</p>

  <div class="bins">
    <div class="bin"><span class="bin__label is-blue">PAPEL</span><span class="bin__icon is-blue"><svg viewBox="0 0 20 20"><path d="M4 7l6-4 6 4M16 13l-6 4-6-4" fill="none" stroke="#fff" stroke-width="2"/></svg></span><div class="bin__items" role="img" aria-label="Ilustração de papéis e caixas"></div></div>
    <div class="bin"><span class="bin__label is-red">PLÁSTICO</span><span class="bin__icon is-red"><svg viewBox="0 0 20 20"><path d="M4 7l6-4 6 4M16 13l-6 4-6-4" fill="none" stroke="#fff" stroke-width="2"/></svg></span><div class="bin__items" role="img" aria-label="Ilustração de garrafas plásticas"></div></div>
    <div class="bin"><span class="bin__label is-green">VIDROS</span><span class="bin__icon is-green"><svg viewBox="0 0 20 20"><path d="M4 7l6-4 6 4M16 13l-6 4-6-4" fill="none" stroke="#fff" stroke-width="2"/></svg></span><div class="bin__items" role="img" aria-label="Ilustração de garrafas e frascos de vidro"></div></div>
    <div class="bin"><span class="bin__label is-yellow">METAL</span><span class="bin__icon is-yellow"><svg viewBox="0 0 20 20"><path d="M4 7l6-4 6 4M16 13l-6 4-6-4" fill="none" stroke="#fff" stroke-width="2"/></svg></span><div class="bin__items" role="img" aria-label="Ilustração de latas de metal"></div></div>
    <div class="bin"><span class="bin__label is-grey">OUTROS</span><span class="bin__icon is-grey"><svg viewBox="0 0 20 20"><path d="M4 7l6-4 6 4M16 13l-6 4-6-4" fill="none" stroke="#fff" stroke-width="2"/></svg></span><div class="bin__items" role="img" aria-label="Ilustração de resíduos diversos"></div></div>
  </div>

  <table class="guide">
    <thead><tr><th>Recicláveis</th><th>Não recicláveis</th></tr></thead>
    <tbody>
      <tr><td class="is-blue">Jornais, revistas e caixas</td><td class="is-blue">Papel sujo e guardanapos</td></tr>
      <tr><td class="is-red">Garrafas PET e potes</td><td class="is-red">Isopor e embalagens metalizadas</td></tr>
      <tr><td class="is-green">Garrafas, frascos e copos</td><td class="is-green">Espelhos e cerâmicas</td></tr>
      <tr><td class="is-yellow">Latas de alumínio e aço</td><td class="is-yellow">Pilhas e clipes</td></tr>
    </tbody>
  </table>

  <p class="note">Separe os resíduos limpos e secos antes da coleta.</p>

  <div class="back-footer"></div>
</section>

</body>
</html>
```